e-commerce store for sport clothing online store "baseball merchandise "web application...

I want to design a UX/UI for my web application website for the online store I will provide you with the following:
1. screen shots of the initial design for the pages>
2. the logo files.
3. The brand guideline file.

the provided files (screen shots) is guideline I want to see CREATIVITY with the UX/UI DESIGN.
PS. PLEASE FOLLOW THE BRANDGUIDE LINE CAREFULLY SPECIALLY THE TYPOGRAPHY & THE COLOR CODES.

PLEASE VISIT THIS WEBSITE morningpath.velrin-qz.com to see more for the screens.

```html
<!DOCTYPE html>
<html lang="en">
<head>
<meta charset="UTF-8">
<title>Basepath – Navigation Drawer</title>
<link rel="stylesheet" href="https://fonts.googleapis.com/css2?family=Titillium+Web:wght@400;600;700&display=swap">
<style>
  :root {
    --navy: #0f2550;
    --navy-deep: #0b1b3c;
    --ink: #0f2550;
    --white: #ffffff;
    --avatar: #f6a44a;
    --dim: rgba(0, 0, 0, 0.5);
    --row: #f4f4f4;
    --card: #ffffff;
    --accent: #b0103a;
    --photo-a: #3c3f3d;
    --photo-b: #6a6d6a;
    --grey-text: #3a3a3a;
  }
  html, body {
    margin: 0;
    padding: 0;
    width: 1200px;
    height: 2673px;
    overflow: hidden;
    background: var(--white);
  }
  .screen {
    position: relative;
    width: 360px;
    height: 802px;
    transform: scale(3.33334);
    transform-origin: 0 0;
    overflow: hidden;
    font-family: "Titillium Web", sans-serif;
    background: var(--white);
  }

  /* ---------- underlying store page ---------- */
  .store { position: absolute; inset: 0; }
  .store-bar { position: absolute; left: 0; top: 0; width: 360px; height: 52px; background: var(--navy); }
  .store-cart { position: absolute; left: 312px; top: 30px; }
  .store-badge {
    position: absolute; left: 326px; top: 25px; width: 14px; height: 14px; border-radius: 50%;
    background: var(--accent); color: var(--white); font-size: 9px; line-height: 14px; text-align: center; font-weight: 600;
  }
  .store-banner {
    position: absolute; left: 0; top: 52px; width: 360px; height: 210px;
    background: linear-gradient(180deg, var(--photo-b), var(--photo-a));
  }
  .store-row {
    position: absolute; left: 0; width: 360px; background: var(--row);
    border-bottom: 1px solid #ddd;
  }
  .store-row svg { position: absolute; left: 331px; }
  .product {
    position: absolute; left: 0; width: 360px; height: 150px; background: var(--card);
  }
  .product-thumb {
    position: absolute; left: 262px; top: 27px; width: 62px; height: 80px;
    background: #e4e4e4; border-radius: 4px; box-shadow: 0 1px 4px rgba(0,0,0,.25);
  }
  .product-title {
    position: absolute; left: 338px; top: 20px; width: 60px; font-size: 12px; font-weight: 700;
    line-height: 15px; color: var(--ink); white-space: nowrap;
  }
  .product-text {
    position: absolute; left: 338px; top: 52px; font-size: 10px; line-height: 12px; color: var(--grey-text);
    white-space: nowrap;
  }
  .product-dot {
    position: absolute; left: 340px; top: 124px; width: 44px; height: 44px; border-radius: 50%; background: var(--accent);
  }
  .scrim { position: absolute; inset: 0; background: var(--dim); }

  /* ---------- drawer ---------- */
  .drawer {
    position: absolute; left: 0; top: 0; width: 269px; height: 802px; background: var(--white);
  }
  .drawer-head {
    position: absolute; left: 0; top: 0; width: 269px; height: 184px; background: var(--navy);
  }
  .back { position: absolute; left: 15px; top: 14px; }
  .avatar {
    position: absolute; left: 28px; top: 40px; width: 72px; height: 72px; border-radius: 50%;
    background: var(--avatar); border: 4px solid var(--white);
  }
  .user-name {
    position: absolute; left: 130px; top: 55px; font-size: 17px; font-weight: 400; color: var(--white); line-height: 22px;
  }
  .user-mail {
    position: absolute; left: 130px; top: 80px; font-size: 11px; color: #dfe5f0; line-height: 14px;
  }
  .menu { list-style: none; margin: 0; padding: 0; }
  .menu-item {
    position: absolute; left: 0; width: 269px; height: 30px; display: flex; align-items: center;
  }
  .menu-icon { position: absolute; left: 28px; width: 20px; height: 20px; }
  .menu-label {
    position: absolute; left: 69px; font-size: 16px; font-weight: 700; color: var(--ink);
  }
  .footer-note {
    position: absolute; left: 0; width: 269px; top: 1470px; text-align: center;
    font-size: 9px; font-weight: 700; color: var(--ink);
  }
</style>
</head>
<body>
<div class="screen">

  <div class="store">
    <div class="store-bar"></div>
    <svg class="store-cart" width="24" height="22" viewBox="0 0 24 22"><path d="M1 2h4l3 11h11l3-8H7" fill="none" stroke="#cfd6e4" stroke-width="2"/><circle cx="9" cy="18" r="2" fill="#cfd6e4"/><circle cx="18" cy="18" r="2" fill="#cfd6e4"/></svg>
    <div class="store-badge">1</div>
    <div class="store-banner" role="img" aria-label="Banner photo of palm trees under a pale sky"></div>

    <div class="store-row" style="top:262px;height:62px;">
      <svg style="top:24px" width="12" height="14" viewBox="0 0 12 14"><path d="M3 1l6 6-6 6" fill="none" stroke="#222" stroke-width="2"/></svg>
    </div>
    <div class="product" style="top:325px;">
      <div class="product-thumb" role="img" aria-label="Product photo of a grey printed t-shirt"></div>
      <div class="product-title">Mis<br>Flyw</div>
      <div class="product-text">If yo<br>your<br>som<br>Labr</div>
      <div class="product-dot"></div>
    </div>
    <div class="store-row" style="top:477px;height:102px;">
      <svg style="top:44px" width="12" height="14" viewBox="0 0 12 14"><path d="M3 1l6 6-6 6" fill="none" stroke="#222" stroke-width="2"/></svg>
    </div>
    <div class="product" style="top:555px;">
      <div class="product-thumb" role="img" aria-label="Product photo of a grey baseball cap"></div>
      <div class="product-title">Bas</div>
      <div class="product-text" style="top:36px">Supe<br>struc<br>buck<br>prof</div>
      <div class="product-dot"></div>
    </div>
    <div class="store-row" style="top:707px;height:95px;">
      <svg style="top:44px" width="12" height="14" viewBox="0 0 12 14"><path d="M3 1l6 6-6 6" fill="none" stroke="#222" stroke-width="2"/></svg>
    </div>
    <div class="scrim"></div>
  </div>

  <nav class="drawer">
    <header class="drawer-head">
      <svg class="back" width="18" height="16" viewBox="0 0 18 16"><path d="M17 8H3M9 1L2 8l7 7" fill="none" stroke="#fff" stroke-width="2"/></svg>
      <div class="avatar" role="img" aria-label="User profile avatar"></div>
      <div class="user-name">User Name</div>
      <div class="user-mail">abc123@fieldmail.com</div>
    </header>

    <ul class="menu">
      <li class="menu-item" style="top:215px;">
        <svg class="menu-icon" viewBox="0 0 20 20"><path d="M10 3L2 10h2.5v7h11v-7H18z" fill="var(--ink)"/></svg>
        <span class="menu-label">Home</span>
      </li>
      <li class="menu-item" style="top:284px;">
        <svg class="menu-icon" viewBox="0 0 20 20"><path d="M1 3h3l2.5 9h9l2.5-7H5.5" fill="none" stroke="var(--ink)" stroke-width="2"/><circle cx="8" cy="16" r="1.6" fill="var(--ink)"/><circle cx="15" cy="16" r="1.6" fill="var(--ink)"/></svg>
        <span class="menu-label">My Cart</span>
      </li>
      <li class="menu-item" style="top:353px;">
        <svg class="menu-icon" viewBox="0 0 20 20"><path d="M1 5h11v9H1zM12 8h4l3 3v3h-7z" fill="var(--ink)"/><circle cx="5" cy="15.5" r="2" fill="var(--ink)" stroke="#fff"/><circle cx="15" cy="15.5" r="2" fill="var(--ink)" stroke="#fff"/></svg>
        <span class="menu-label">Track Oders</span>
      </li>
      <li class="menu-item" style="top:421px;">
        <svg class="menu-icon" viewBox="0 0 20 20"><circle cx="10" cy="10" r="6" fill="var(--ink)"/><g stroke="var(--ink)" stroke-width="3"><path d="M10 1.5v3M10 15.5v3M1.5 10h3M15.5 10h3M4 4l2 2M14 14l2 2M16 4l-2 2M4 16l2-2"/></g><circle cx="10" cy="10" r="2.3" fill="#fff"/></svg>
        <span class="menu-label">Settings</span>
      </li>
      <li class="menu-item" style="top:493px;">
        <svg class="menu-icon" viewBox="0 0 20 20"><circle cx="7" cy="6" r="3.5" fill="var(--ink)"/><path d="M0.5 18c0-4 3-6.5 6.5-6.5s6.5 2.5 6.5 6.5z" fill="var(--ink)"/><path d="M14 7h5M15 10.5h4M16 14h3" stroke="var(--ink)" stroke-width="1.6"/></svg>
        <span class="menu-label">Contact</span>
      </li>
      <li class="menu-item" style="top:561px;">
        <svg class="menu-icon" viewBox="0 0 20 20"><rect x="1.5" y="1.5" width="15" height="17" fill="var(--ink)"/><path d="M5 10h9M10.5 6.5L14 10l-3.5 3.5" fill="none" stroke="#fff" stroke-width="1.8"/></svg>
        <span class="menu-label">Log Out</span>
      </li>
    </ul>

    <div class="footer-note" style="top:770px;">© Basepath 2022</div>
  </nav>

</div>
</body>
</html>
```